11 x 17 Orvanthes Quote

Design the following quote in a poster.

"First say to yourself what you would be; then do what you have to do." - Orvanthes

See here for inspiration - https://prints.mornbrekal.com/

Quote

```html
<!DOCTYPE html>
<html lang="en">
<head>
<meta charset="utf-8">
<title>Orvanthes Quote Poster</title>
<link rel="stylesheet" href="https://fonts.googleapis.com/css2?family=Kaushan+Script&display=swap">
<style>
  :root {
    --ink: #ffffff;
    --say: #d63a2c;
    --be: #2f8fca;
    --do: #eaa94c;
    --sky-top: #0d1024;
    --sky-mid: #18224a;
    --sky-teal: #1f4d63;
    --sky-rose: #8a2f55;
    --sky-glow: #e8685a;
  }
  html, body {
    margin: 0;
    padding: 0;
    overflow: hidden;
    background: var(--sky-top);
  }
  .poster {
    position: relative;
    width: 783px;
    height: 1200px;
    overflow: hidden;
    font-family: "Kaushan Script", cursive;
    color: var(--ink);
  }
  .poster__sky {
    position: absolute;
    inset: 0;
    background:
      radial-gradient(ellipse 90% 30% at 90% 105%, var(--sky-glow) 0%, rgba(232,104,90,0.5) 35%, transparent 75%),
      radial-gradient(ellipse 80% 60% at 0% 35%, rgba(31,77,99,0.9) 0%, transparent 70%),
      linear-gradient(172deg, var(--sky-top) 0%, var(--sky-mid) 45%, #2b2550 68%, var(--sky-rose) 88%, var(--sky-glow) 100%);
  }
  .quote {
    position: absolute;
    inset: 0;
    margin: 0;
  }
  .quote__line {
    position: absolute;
    left: 0;
    right: 0;
    text-align: center;
    line-height: 1;
    font-size: 62px;
    letter-spacing: 2px;
    transform: translateY(-50%);
    white-space: nowrap;
  }
  .quote__line--key {
    font-size: 76px;
    letter-spacing: 3px;
  }
  .quote__line--say { color: var(--say); }
  .quote__line--be  { color: var(--be); }
  .quote__line--do  { color: var(--do); }
  .quote__author {
    position: absolute;
    left: 0;
    right: 0;
    top: 1080px;
    transform: translateY(-50%);
    text-align: center;
    font-size: 70px;
    line-height: 1;
    font-style: normal;
  }
</style>
</head>
<body>
  <main class="poster">
    <div class="poster__sky" role="img" aria-label="Starry night sky fading from deep navy to a rose and coral glow"></div>
    <blockquote class="quote">
      <span class="quote__line" style="top:130px">First</span>
      <span class="quote__line quote__line--key quote__line--say" style="top:241px">SAY</span>
      <span class="quote__line" style="top:357px">to yourself</span>
      <span class="quote__line" style="top:468px">what you would</span>
      <span class="quote__line quote__line--key quote__line--be" style="top:580px">BE</span>
      <span class="quote__line" style="top:691px">then do what you</span>
      <span class="quote__line" style="top:802px">have to</span>
      <span class="quote__line quote__line--key quote__line--do" style="top:913px">DO</span>
      <cite class="quote__author">Orvanthes</cite>
    </blockquote>
  </main>
</body>
</html>
```